Gutschein-Design für kleines Restaurant in Niederbayern
Zielgruppe
Wir sind ein kleines Restaurant in Niederbayern mit modern/rustikaler Einrichtung und bodenständiger, regionaler Küche. Unsere Zielgruppe sind Gäste mittleren bis höheren Alters zum teil auch gut situiert.
Aufgabenstellung
Der Gutschein soll eher schlicht und natürlich wirken in DIN Lang (Querformat), nicht aufklappbar. Die Schrift darf gerne etwas verspeilt sein. Wir möchten den Gutschein auf weißes Papier drucken mit Kraftpapier-Umschlag. Blätter in zwei Ecken des Gutscheins wären toll, evtl. mit braunen Pampasgras (Vorderseite gerne auch Rückseite) (siehe Bild). Der Gutschein sollte auf der Vorderseite in der Mitte das Logo enthalten. Der Gutschein muss folgende Daten enthalten: Anschrift mit Telefon und email, Gutschein-Nummer (klein), Ausstellungs-Datum (klein), Betrag, keine Barauszahlung möglich' (klein), Für wen er bestimmt ist.
Hier unsere Daten:
Restaurant Lomberg
Kirchgasse 27
94281 Bergried
info@restaurant-lomberg-beispiel.de

```html
<!DOCTYPE html>
<html lang="de">
<head>
<meta charset="utf-8">
<title>Gutschein – Restaurant Lomberg</title>
<link rel="stylesheet" href="https://fonts.googleapis.com/css2?family=Crimson+Pro:wght@400;600&display=swap">
<style>
  :root {
    --paper: #ecebe8;
    --paper-shade: #e3e2de;
    --ink: #3f3c40;
    --frame: #d9bf9f;
    --pampas: #dcc4a4;
    --slate: #6d7078;
  }
  html, body {
    margin: 0;
    padding: 0;
    width: 1200px;
    height: 600px;
    overflow: hidden;
    background: var(--paper);
  }
  .voucher {
    position: relative;
    width: 1200px;
    height: 600px;
    overflow: hidden;
    background: radial-gradient(ellipse at 50% 50%, var(--paper) 60%, var(--paper-shade) 100%);
    font-family: "Crimson Pro", "EB Garamond", Georgia, serif;
    color: var(--ink);
  }
  .frame {
    position: absolute;
    inset: 0;
    width: 1200px;
    height: 600px;
  }
  .floral { position: absolute; }
  .floral--top-right {
    left: 880px;
    top: -10px;
    width: 330px;
    height: 345px;
    border-radius: 45% 10% 40% 60% / 30% 10% 60% 60%;
    background:
      radial-gradient(ellipse 18% 40% at 62% 45%, rgba(109,112,120,0.55), transparent 70%),
      radial-gradient(ellipse at 60% 35%, var(--pampas) 0%, rgba(220,196,164,0.7) 45%, transparent 75%);
  }
  .floral--bottom-left {
    left: -10px;
    top: 262px;
    width: 330px;
    height: 345px;
    border-radius: 55% 45% 10% 10% / 60% 40% 10% 10%;
    background:
      radial-gradient(ellipse 18% 40% at 35% 55%, rgba(109,112,120,0.55), transparent 70%),
      radial-gradient(ellipse at 38% 65%, var(--pampas) 0%, rgba(220,196,164,0.7) 45%, transparent 75%);
  }
  .title {
    position: absolute;
    left: 0;
    right: 0;
    top: 78px;
    margin: 0;
    padding-right: 38px;
    text-align: center;
    font-weight: 400;
    font-size: 86px;
    letter-spacing: 3px;
    line-height: 1;
  }
  .field {
    position: absolute;
    font-size: 25px;
    line-height: 1;
  }
  .field__label { position: absolute; }
  .field__line {
    position: absolute;
    height: 0;
    border-top: 1.5px solid var(--ink);
  }
  .field--amount .field__label { left: 305px; top: 258px; }
  .field--amount .field__line { left: 374px; width: 410px; top: 277px; }
  .field--amount .field__unit { position: absolute; left: 798px; top: 260px; }
  .field--recipient .field__label { left: 317px; top: 352px; }
  .field--recipient .field__line { left: 374px; width: 410px; top: 369px; }
  .contact {
    position: absolute;
    left: 0;
    right: 0;
    top: 445px;
    text-align: center;
    font-size: 21.5px;
    line-height: 28px;
    font-style: normal;
  }
  .contact__name { font-weight: 600; display: block; }
  .side-note {
    position: absolute;
    white-space: nowrap;
    transform: rotate(-90deg);
    transform-origin: left top;
  }
  .side-note--number { left: 45px; top: 160px; font-size: 13px; }
  .side-note--cash { left: 1145px; top: 556px; font-size: 15.5px; }
</style>
</head>
<body>
<main class="voucher">
  <svg class="frame" viewBox="0 0 1200 600" aria-hidden="true">
    <g fill="none" stroke="var(--frame)" stroke-width="2">
      <polyline points="930,31 31,31 31,370"/>
      <polyline points="278,569 1169,569 1169,224"/>
    </g>
  </svg>

  <div class="floral floral--top-right" role="img" aria-label="Aquarell mit Pampasgras und Eukalyptusblättern in Beige und Schiefergrau"></div>
  <div class="floral floral--bottom-left" role="img" aria-label="Aquarell mit Pampasgras und Eukalyptusblättern in Beige und Schiefergrau"></div>

  <span class="side-note side-note--number">Nummer:</span>

  <h1 class="title">GUTSCHEIN</h1>

  <div class="field field--amount">
    <span class="field__label">über</span>
    <span class="field__line"></span>
    <span class="field__unit">Euro</span>
  </div>

  <div class="field field--recipient">
    <span class="field__label">für</span>
    <span class="field__line"></span>
  </div>

  <address class="contact">
    <span class="contact__name">Restaurant Lomberg</span>
    Kirchgasse 27 · 94281 Bergried<br>
    08871/5518207 · info@restaurant-lomberg-beispiel.de
  </address>

  <span class="side-note side-note--cash">keine Barauszahlung möglich</span>
</main>
</body>
</html>
```